Luxury interior design firm needs a pagecraft

We are a new firm, requiring an initial pagecraft design that we will be able to update ourselves following completion of the project. We are an Australian firm targeting a market segment with an affinity for luxury brands. We successfully attained a logo through pixel harbor that matched our criteria of 'elegant' 'masculine' and 'sophisticated'. We received the font that was used to create the logo and can provide it to the pagecraft designer to create 'buttons' on the page.
Reference website: www.corbinashfieldvane.example
The navigation of the site should be as follows:
HOME PAGE:
Logo centred at ¼ from top (large)
Above logo: smaller buttons using same font as logo,
Hovering over each button should result in a highlighted blue bar above/below the word in same colour as ‘DESIGN’ in logo
Buttons: ‘PROFILE’, ‘PORTFOLIO’, ‘BLOG’, ‘CONTACT’
Majority of page taken up by photos of portfolio work, fading, (not right-to-left)
Bottom of page: Links to Chatterbook, Clipboardly, Snapgrove
For remaining pages, logo and buttons to move upwards further towards the top of the page. Logo to act as hyperlink back to home page.
‘PROFILE’ PAGE:
Photo to take up top-right ¼ of page
Text to the left of photo, before filling width of page when it gets lower than the bottom edge of the photo
‘PORTFOLIO’ PAGE:
Photo album, with medium size thumbnails
Hovering over each thumbnail should result in a blue bar below the photo, same as the buttons at top of page
Clicking on each thumbnail should result in a large pop-up of that photo in the centre of the screen
User should be able to navigate left and right through album without having to return to thumbnail gallery
Left/right navigation arrows should appear when the user hovers cursor in the approximate area, and disappear when not in use
‘BLOG’ PAGE:
Should follow the format of a clipboardly or pagecraft photo blog page
Photo album with captions underneath each
Most recent posts at the top/left
? Is it possible to just embed our clipboardly page?
‘CONTACT’
Box in centre of page with contact details
Photos scrolling in the background as per home page, but substantially faded out.
Target Market(s)
High net-worth clients who have a strong association with luxury brands such as Valorne, Cadence Morrell, Arventa. Mostly middle-aged females who are drawn to a slightly more masculine brand (relative to competitors).
Look and feel
Each slider illustrates characteristics of the customer's brand and the style your logo design should communicate.

```html
<!DOCTYPE html>
<html lang="en">
<head>
<meta charset="utf-8">
<title>Hollis Marr Design — Blog</title>
<link rel="stylesheet" href="https://fonts.googleapis.com/css2?family=Jost:wght@300;400&family=Arimo:wght@400&display=swap">
<style>
  :root {
    --ink: #111111;
    --nav-bg: #000000;
    --nav-text: #ffffff;
    --accent: #1a8ad6;
    --band: rgba(232, 232, 232, 0.96);
    --card: rgba(236, 236, 236, 0.96);
    --card-edge: #f6f6f6;
    --meta: #555555;
    --body: #2a2a2a;
    --footer-bg: #ffffff;
  }
  * { box-sizing: border-box; margin: 0; padding: 0; }
  html, body { width: 1104px; height: 1200px; overflow: hidden; }
  body { position: relative; background: #1a1a1a; font-family: "Arimo", Arial, sans-serif; color: var(--body); }

  .site-nav { position: absolute; top: 0; left: 0; width: 1104px; height: 50px; background: var(--nav-bg); }
  .site-nav a { position: absolute; top: 16px; transform: translateX(-50%); color: var(--nav-text); text-decoration: none;
    font-family: "Jost", sans-serif; font-weight: 400; font-size: 18px; letter-spacing: 1.6px; }
  .site-nav .active-bar { position: absolute; left: 436px; top: 50px; width: 175px; height: 4px; background: var(--accent); }
  .social { position: absolute; right: 38px; top: 16px; display: flex; gap: 12px; }
  .social a { position: static; transform: none; font-size: 12px; letter-spacing: 0.4px; display: flex; align-items: center; gap: 5px; }
  .social a::before { content: ""; width: 8px; height: 8px; border-radius: 50%; background: var(--nav-text); }

  .brand-band { position: absolute; top: 54px; left: 0; width: 1104px; height: 68px; background: var(--band); border-top: 2px solid #c9c9c9; }
  .brand { position: absolute; left: 82px; top: 2px; width: 944px; display: flex; justify-content: space-between;
    font-family: "Jost", sans-serif; font-weight: 300; font-size: 52px; color: var(--ink); text-decoration: none; line-height: 60px; }

  .backdrop { position: absolute; top: 122px; left: 0; width: 1104px; height: 1008px;
    background: linear-gradient(180deg, #8c8780 0%, #5a534c 22%, #3a332d 45%, #1c1815 70%, #0c0b0a 100%); }

  .card { position: absolute; width: 304px; background: var(--card); border: 1px solid var(--card-edge);
    box-shadow: 0 1px 3px rgba(0,0,0,0.3); padding: 20px 10px 0 10px; }
  .card h2 { font-family: "Jost", sans-serif; font-weight: 400; font-size: 18px; letter-spacing: 1.6px; color: #222;
    padding-left: 13px; line-height: 24px; }
  .card .meta { font-size: 11.5px; color: var(--meta); padding-left: 15px; margin-top: 1px; word-spacing: 1px; }
  .card .meta span { margin: 0 10px; }
  .card .photo { width: 285px; height: 133px; margin-top: 16px; }
  .card .photo.tall { height: 211px; }
  .card p { font-size: 13px; line-height: 19.2px; margin: 13px 5px 0 5px; text-align: justify; }
  .card p + p { margin-top: 5px; }
  .card .more { display: block; margin: 9px 5px 0 5px; font-size: 13px; color: var(--accent); text-decoration: none; font-style: italic; }

  .site-footer { position: absolute; top: 1130px; left: 0; width: 1104px; height: 70px; background: var(--footer-bg); text-align: center;
    font-family: "Jost", sans-serif; font-size: 13px; letter-spacing: 1.2px; color: #111; }
  .site-footer nav { margin-top: 19px; }
  .site-footer nav a { color: #111; text-decoration: none; }
  .site-footer nav .sep { margin: 0 12px; font-size: 10px; }
  .site-footer small { display: block; margin-top: 8px; font-size: 12.5px; }
</style>
</head>
<body>
  <nav class="site-nav">
    <a href="#" style="left:170px">PROFILE</a>
    <a href="#" style="left:347px">PORTFOLIO</a>
    <a href="#" style="left:523px">BLOG</a>
    <a href="#" style="left:700px">CONTACT</a>
    <span class="active-bar"></span>
    <div class="social">
      <a href="#">Chatterbook</a>
      <a href="#">Snapgrove</a>
      <a href="#">Clipboardly</a>
    </div>
  </nav>

  <header class="brand-band">
    <a class="brand" href="#"><span>H</span><span>O</span><span>L</span><span>L</span><span>I</span><span>S</span><span>&nbsp;</span><span>M</span><span>A</span><span>R</span><span>R</span><span>&nbsp;</span><span>D</span><span>E</span><span>S</span><span>I</span><span>G</span><span>N</span></a>
  </header>

  <div class="backdrop" role="img" aria-label="Dim luxury interior background photograph"></div>

  <main>
    <article class="card" style="left:84px;top:149px;height:364px">
      <h2>DONEC CURSUS MATTIS</h2>
      <div class="meta">May-13-2013<span>|</span>10.15 a.m<span>|</span>6 comments</div>
      <div class="photo" role="img" aria-label="Fashion photo of a woman with a designer handbag" style="background:linear-gradient(120deg,#2a1a16,#6b4a36 55%,#c9b8a6)"></div>
      <p>Nunc sagittis, felis eleifend sodales pulvinar, neque ipsum fermentum mauris, quis blandit erat nisl quis nisl. Ut ullamcorper bibendum dui sed tristique senectus et netus et malesuada fames ac turpis egestas.</p>
      <a class="more" href="#">More »</a>
    </article>

    <article class="card" style="left:84px;top:524px;height:556px">
      <h2>DONEC CURSUS MATTIS</h2>
      <div class="meta">May-13-2013<span>|</span>10.15 a.m<span>|</span>6 comments</div>
      <div class="photo tall" role="img" aria-label="Black sports car in a lit showroom" style="background:linear-gradient(180deg,#3a2a1c,#0e0e0e 55%,#b8b8bc)"></div>
      <p style="margin-top:26px">Nunc sagittis, felis eleifend sodales pulvinar, neque ipsum fermentum mauris, quis blandit erat nisl quis nisl. Ut ullamcorper bibendum dui sed tristique senectus et netus et malesuada fames ac turpis egestas. Etiam mattis odio ut lectus bibendum gravida. Cras imperdiet felis sit amet ipsum laoreet tempus. Quisque mauris nulla, viverra eget sodales vitae, ornare eu nisi. Etiam tristique accumsan dictum. In eget urna pretium urna iaculis congue eget ac velit. Sed hendrerit porttitor volutpat.</p>
      <a class="more" href="#">More »</a>
    </article>

    <article class="card" style="left:400px;top:149px;height:412px">
      <h2>DONEC CURSUS MATTIS</h2>
      <div class="meta">May-13-2013<span>|</span>10.15 a.m<span>|</span>6 comments</div>
      <div class="photo" role="img" aria-label="Legs in black heels in a bright hallway" style="background:linear-gradient(110deg,#d8cbb0,#8a8680 55%,#c4c6cc)"></div>
      <p>Nunc sagittis, felis eleifend sodales pulvinar, neque ipsum fermentum mauris, quis blandit erat nisl quis nisl. Ut ullamcorper bibendum.</p>
      <p>Class aptent taciti sociosqu ad litora torquent per conubia nostra, per inceptos himenaeos. In conval-lis elit eget orci volutpat interdum. Donec tincidunt velit non tellus semper pretium.</p>
      <a class="more" href="#" style="margin-top:14px">More »</a>
    </article>

    <article class="card" style="left:400px;top:572px;height:306px">
      <h2>DONEC CURSUS MATTIS</h2>
      <div class="meta">May-13-2013<span>|</span>10.15 a.m<span>|</span>6 comments</div>
      <div class="photo" role="img" aria-label="Cut gemstone on a dark background" style="background:radial-gradient(ellipse at center,#e8d6c8 0%,#9a5a3a 35%,#1a0e08 70%)"></div>
      <p>Nunc sagittis, felis eleifend sodales pulvinar, neque ipsum fermentum mauris, quis.</p>
      <a class="more" href="#">More »</a>
    </article>

    <article class="card" style="left:400px;top:890px;height:220px">
      <h2>DONEC CURSUS MATTIS</h2>
      <div class="meta">May-13-2013<span>|</span>10.15 a.m<span>|</span>6 comments</div>
      <div class="photo" role="img" aria-label="Fashion photo of a reclining woman in pale tones" style="background:linear-gradient(130deg,#cfc4c0,#e6dcd8 50%,#b8a8a8)"></div>
    </article>

    <article class="card" style="left:718px;top:149px;height:325px">
      <h2>DONEC CURSUS MATTIS</h2>
      <div class="meta">May-13-2013<span>|</span>10.15 a.m<span>|</span>6 comments</div>
      <div class="photo" role="img" aria-label="Women shopping in a boutique" style="background:linear-gradient(90deg,#d4d0cc,#9c8c84 45%,#6a3c4a)"></div>
      <p>Nunc sagittis, felis eleifend sodales pulvinar, neque ipsum fermentum mauris, quis blandit erat nisl quis nisl. Ut ullamcorper bibendum dui sed tristique</p>
      <a class="more" href="#">More »</a>
    </article>

    <article class="card" style="left:718px;top:486px;height:287px">
      <h2>DONEC CURSUS MATTIS</h2>
      <div class="meta">May-13-2013<span>|</span>10.15 a.m<span>|</span>6 comments</div>
      <div class="photo" role="img" aria-label="Friends carrying shopping bags" style="background:linear-gradient(100deg,#6a7a4a,#d89a6a 45%,#e8b830)"></div>
      <p>Nunc sagittis, felis eleifend sodales pulvinar.</p>
      <a class="more" href="#">More »</a>
    </article>

    <article class="card" style="left:718px;top:784px;height:326px">
      <h2>DONEC CURSUS MATTIS</h2>
      <div class="meta">May-13-2013<span>|</span>10.15 a.m<span>|</span>6 comments</div>
      <div class="photo" role="img" aria-label="Two women in fashion outfits outdoors" style="background:linear-gradient(110deg,#8a6a4a,#c8a880 45%,#2a3040)"></div>
      <p>Nunc sagittis, felis eleifend sodales pulvinar, neque ipsum fermentum mauris, quis blandit erat nisl quis nisl. Ut ullamcorper bibendum dui sed tristique</p>
      <a class="more" href="#">More »</a>
    </article>
  </main>

  <footer class="site-footer">
    <nav>
      <a href="#">HOME</a><span class="sep">::</span><a href="#">PROFILE</a><span class="sep">::</span><a href="#">PORTFOLIO</a><span class="sep">::</span><a href="#">BLOG</a><span class="sep">::</span><a href="#">CONTACT</a>
    </nav>
    <small>COPYRIGHT &nbsp;© &nbsp;2013 HOLLIS MARR DESIGN &nbsp;&nbsp;&nbsp;ALL RIGHTS RESERVED.</small>
  </footer>
</body>
</html>
```